New modern business card design

To design a brand new business card that's clean & modern in terms of layout.
I have attached our company logo and also basic information regarding what is needed on the card that also needs to be editable.

Target Market(s)

motor trade

Contact Information for Business Card

logo, name, title, tel, mob, email, address, www, all information is in the word.doc file

Requirements
Must have
• white background
Nice to have
• Nice clean font

```html
<!DOCTYPE html>
<html lang="en">
<head>
<meta charset="utf-8">
<title>Torque Fixings Ltd – Business Card</title>
<link rel="stylesheet" href="https://fonts.googleapis.com/css2?family=Michroma&family=Open+Sans:wght@400&display=swap">
<style>
  :root {
    --brand-blue: #1f74c1;
    --card-white: #ffffff;
    --ink: #3b3b3b;
    --backdrop: #3d3d3d;
    --rule-grey: #c8c8c8;
    --rule-light: rgba(255,255,255,0.22);
  }
  * { margin: 0; padding: 0; box-sizing: border-box; }
  html, body { width: 1200px; height: 802px; overflow: hidden; }
  body { background: var(--backdrop); position: relative; font-family: "Open Sans", sans-serif; }

  .card {
    position: absolute;
    top: 274px;
    width: 442px;
    height: 265px;
    overflow: hidden;
    box-shadow: 0 3px 8px rgba(0,0,0,0.45);
  }
  .card--front { left: 136px; background: var(--card-white); }
  .card--back { left: 624px; background: var(--brand-blue); }

  .brand {
    position: absolute;
    left: 20px;
    top: 108px;
    width: 176px;
    display: flex;
    align-items: center;
    justify-content: center;
    gap: 7px;
  }
  .brand__square { width: 11px; height: 11px; background: var(--brand-blue); flex: none; }
  .brand__name {
    font-family: "Michroma", sans-serif;
    font-size: 12.5px;
    color: var(--brand-blue);
    white-space: nowrap;
  }

  .divider {
    position: absolute;
    left: 212px;
    top: 63px;
    width: 1px;
    height: 138px;
    background: var(--rule-grey);
  }

  .contact { position: absolute; left: 229px; top: 59px; width: 200px; color: var(--ink); }
  .contact__name {
    font-family: "Michroma", sans-serif;
    font-weight: 400;
    font-size: 13.5px;
    color: var(--brand-blue);
    line-height: 21px;
    white-space: nowrap;
  }
  .contact__title { font-size: 12.5px; line-height: 16px; }
  .contact__list { list-style: none; margin-top: 4px; }
  .contact__list li {
    font-size: 12.5px;
    line-height: 15.5px;
    display: flex;
    align-items: center;
    gap: 3px;
    white-space: nowrap;
  }
  .contact__list svg { width: 10px; height: 10px; fill: var(--brand-blue); flex: none; }
  .contact__address { font-size: 12.5px; line-height: 15.5px; margin-top: 6px; font-style: normal; }
  .contact__web { font-size: 12.5px; line-height: 16px; color: var(--brand-blue); text-decoration: none; display: block; }

  .back__name {
    position: absolute;
    left: 0; right: 0;
    top: 104px;
    text-align: center;
    font-family: "Michroma", sans-serif;
    font-size: 26px;
    color: var(--card-white);
    white-space: nowrap;
  }
  .back__rule {
    position: absolute;
    left: 97px;
    top: 201px;
    width: 244px;
    height: 1px;
    background: var(--rule-light);
  }
  .back__web {
    position: absolute;
    left: 0; right: 0;
    top: 216px;
    text-align: center;
    font-family: "Michroma", sans-serif;
    font-size: 11.5px;
    color: var(--card-white);
  }
</style>
</head>
<body>
  <section class="card card--front">
    <div class="brand">
      <span class="brand__square"></span>
      <span class="brand__name">TORQUE FIXINGS</span>
    </div>

    <div class="divider"></div>

    <div class="contact">
      <h1 class="contact__name">DANIEL WHITMORE</h1>
      <p class="contact__title">General Manager</p>
      <ul class="contact__list">
        <li>
          <svg viewBox="0 0 10 10" aria-hidden="true"><path d="M1 3.2C1 2 2.5 1.2 5 1.2S9 2 9 3.2V4H7V3.1H3V4H1Z M2.2 4.6h5.6L8.6 8.6H1.4Z"/></svg>
          0161 555 0182
        </li>
        <li>
          <svg viewBox="0 0 10 10" aria-hidden="true"><path d="M3 0.5h4a0.8 0.8 0 0 1 0.8 0.8v7.4a0.8 0.8 0 0 1-0.8 0.8H3a0.8 0.8 0 0 1-0.8-0.8V1.3A0.8 0.8 0 0 1 3 0.5Zm0.4 1.2v6h3.2v-6Z"/></svg>
          07700 900 418
        </li>
        <li>
          <svg viewBox="0 0 10 10" aria-hidden="true"><path d="M0.8 2.2h8.4v5.6H0.8Zm0.8 0.6L5 5.4 8.4 2.8Z"/></svg>
          dwhitmore@torque-fixings.co.uk
        </li>
      </ul>
      <address class="contact__address">
        Kestrel Road<br>
        Denton, Manchester<br>
        M12 9QX
      </address>
      <a class="contact__web" href="#">www.torque-fixings.co.uk</a>
    </div>
  </section>

  <section class="card card--back">
    <p class="back__name">TORQUE FIXINGS</p>
    <div class="back__rule"></div>
    <p class="back__web">WWW.TORQUE-FIXINGS.CO.UK</p>
  </section>
</body>
</html>
```